drafting business needs a 2 sided rack card design. Size specificaton

Document Trim Size:
Full Bleed Size (starting document size)
3.86" x 8.39"
When trimmed the Rack cards are 3.74" x 8.27".
300 DPI

I need my logo, product info, and 2 pictures included

This is product information that i need:

- Floor Plans measured to QERT & PLUX standards
- Stunning HD Photography
- Vexolith - your space delivered in perfect 3D
- E &O insured
- Our products delivered next by before 10:00 AM

It also has to my my special offer: Save 50% off Vexolith, Floor Plans, and Photography

My contact info is
www.quillfenstudio.com
dorian@quillfenstudio.com
778-514-0962
Updates

Hey designers, the common element I see in most of the designs that I actually don't like is the use of orange and blue. I think there was some miscommunication. Please Don't use these colors. It really makes the designs Look cheap. I want a clean, high end look.

Target Market(s)

realtors

Industry/Entity Type

Real Estate

Font styles to use
Serif

Colors

Designer to choose colors to be used in the design.

Requirements
Must have
• At least 2 photos and my logo included. it must include all my wording with discount in bold, but classy.
Nice to have
• I want clean classy design. My logo is and 2 photos should be in design. I design should match my logo colors, I think. I have tons of other photos if you think these arent very useful
• Also I have attached a logo from vexolith. Please include this, but smaller than the Quillfen Studio. The Vexolith is just equiptment that I use
Should not have
• This is a discount promotion, but I dont want it to look cheap whatsoever

```html
<!DOCTYPE html>
<html lang="en">
<head>
<meta charset="utf-8">
<title>Quillfen Studio Rack Cards</title>
<link href="https://fonts.googleapis.com/css2?family=Playfair+Display:wght@400;700;900&family=Lora:wght@400;600&display=swap" rel="stylesheet">
<style>
  :root {
    --bg: #ececec;
    --charcoal: #2a2a2d;
    --graphite: #3d3d42;
    --gold: #b08d57;
    --gold-light: #cdb48a;
    --stone: #7d7873;
    --rule: #d6d2cc;
    --ink: #2a2a2d;
    --ivory: #fbf9f5;
    --white: #ffffff;
  }
  * { box-sizing: border-box; margin: 0; padding: 0; }
  html, body { width: 711px; height: 1200px; overflow: hidden; background: var(--bg); }
  .sheet { position: relative; width: 711px; height: 1200px; }
  .rack-card {
    position: absolute; top: 250px; width: 322px; height: 700px;
    background: var(--ivory); overflow: hidden;
    box-shadow: 0 3px 10px rgba(0,0,0,.25);
    font-family: "Lora", serif;
  }
  .rack-card--front { left: 24px; }
  .rack-card--back { left: 365px; }
  .photo { position: absolute; left: 0; top: 80px; width: 322px; height: 300px; }
  .photo--living { background: linear-gradient(160deg, #e9eef2 0%, #c9c3b6 40%, #8c7a64 75%, #5b4a3a 100%); }
  .photo--entry { background: linear-gradient(150deg, #6a3a1f 0%, #a7a49a 35%, #e6e2da 60%, #8a5030 100%); }
  .shapes { position: absolute; inset: 0; width: 322px; height: 700px; }
  .brand { position: absolute; top: 12px; left: 0; width: 100%; text-align: center; }
  .brand-mark { display: block; width: 52px; height: 52px; margin: 0 auto; border-radius: 50%; background: var(--charcoal); }
  .brand-name { display: block; margin-top: 6px; font-family: "Playfair Display", serif; font-weight: 400; font-size: 21px; color: var(--charcoal); }
  .offer { position: absolute; top: 392px; width: 100%; text-align: center; line-height: 1; }
  .offer-special { font-family: "Playfair Display", serif; font-weight: 400; font-size: 44px; color: var(--stone); letter-spacing: 3px; }
  .offer-main { font-family: "Playfair Display", serif; font-weight: 900; font-size: 56px; color: var(--charcoal); margin-top: 4px; letter-spacing: 2px; }
  .offer-save { font-family: "Playfair Display", serif; font-size: 26px; color: var(--stone); margin-top: 6px; letter-spacing: 1px; }
  .offer-save strong { font-weight: 900; color: var(--gold); }
  .services { position: absolute; top: 546px; left: 0; width: 100%; display: flex; }
  .service { flex: 1; text-align: center; font-size: 10px; letter-spacing: .5px; color: var(--ink); }
  .service + .service { border-left: 1px solid var(--rule); }
  .service svg { display: block; margin: 4px auto 14px; }
  .info-title {
    position: absolute; top: 400px; left: 52px; width: 232px; height: 36px;
    border-radius: 18px; background: var(--charcoal); color: var(--white);
    font-family: "Playfair Display", serif; font-weight: 700; font-size: 17px;
    text-align: center; line-height: 36px; letter-spacing: .5px;
    box-shadow: 0 3px 4px rgba(0,0,0,.25);
  }
  .info-list { position: absolute; top: 458px; width: 100%; list-style: none; text-align: center; font-size: 11px; color: var(--ink); line-height: 20px; }
  .partner { position: absolute; top: 575px; width: 100%; display: flex; justify-content: center; align-items: center; gap: 8px; }
  .partner-mark { width: 20px; height: 20px; background: var(--graphite); }
  .partner-name { font-family: "Lora", serif; font-size: 26px; font-weight: 400; color: var(--graphite); }
  .contact { position: absolute; top: 660px; left: 16px; font-size: 8.5px; color: var(--white); line-height: 15px; list-style: none; }
  .contact li::before { content: ""; display: inline-block; width: 8px; height: 8px; border-radius: 50%; background: var(--gold-light); margin-right: 5px; vertical-align: -1px; }
  .phone { position: absolute; top: 662px; right: 14px; display: flex; align-items: center; gap: 5px; font-family: "Playfair Display", serif; font-weight: 700; font-size: 19px; color: var(--white); }
</style>
</head>
<body>
<main class="sheet">

  <section class="rack-card rack-card--front">
    <div class="photo photo--living" role="img" aria-label="Bright living room with white sofa, large windows and rug"></div>
    <svg class="shapes" viewBox="0 0 322 700" aria-hidden="true">
      <defs>
        <linearGradient id="hdrF" x1="0" y1="0" x2="0" y2="1"><stop offset="0" stop-color="#d8d5d0"/><stop offset="1" stop-color="#fbf9f5"/></linearGradient>
      </defs>
      <path d="M0 0H322V86Q161 130 0 86Z" fill="url(#hdrF)"/>
      <path d="M0 86Q161 130 322 86" stroke="#b08d57" stroke-width="5" fill="none"/>
      <path d="M0 104Q161 132 322 96" stroke="#b08d57" stroke-width="1.5" fill="none"/>
      <path d="M0 382Q161 340 322 382V700H0Z" fill="#fbf9f5"/>
      <path d="M0 378Q161 332 322 378" stroke="#b08d57" stroke-width="5" fill="none"/>
      <path d="M0 365Q161 335 322 370" stroke="#b08d57" stroke-width="1.5" fill="none"/>
      <path d="M0 652Q161 612 322 652V700H0Z" fill="#2a2a2d"/>
      <path d="M0 647Q161 606 322 647" stroke="#b08d57" stroke-width="4" fill="none"/>
    </svg>
    <header class="brand"><span class="brand-mark"></span><span class="brand-name">Quillfen Studio</span></header>
    <div class="offer">
      <p class="offer-special">SPECIAL</p>
      <p class="offer-main">OFFER</p>
      <p class="offer-save">SAVE <strong>50% OFF</strong></p>
    </div>
    <div class="services">
      <div class="service">
        <svg width="44" height="44" viewBox="0 0 46 46"><circle cx="23" cy="23" r="22" fill="#2a2a2d"/><path d="M23 11L33 16V29L23 35L13 29V16Z M13 16L23 21L33 16 M23 21V35" stroke="#cdb48a" stroke-width="2" fill="none"/></svg>
        VEXOLITH
      </div>
      <div class="service">
        <svg width="44" height="44" viewBox="0 0 46 46"><circle cx="23" cy="23" r="22" fill="#2a2a2d"/><path d="M13 13H33V33H13Z M23 13V26 M13 22H20 M26 26H33 M23 30V33" stroke="#cdb48a" stroke-width="2" fill="none"/></svg>
        FLOOR PLANS
      </div>
      <div class="service">
        <svg width="44" height="44" viewBox="0 0 46 46"><circle cx="23" cy="23" r="22" fill="#2a2a2d"/><path d="M12 14H34V32H12Z M14 29L20 22L25 27L28 24L32 29" stroke="#cdb48a" stroke-width="2" fill="none"/><circle cx="28" cy="19" r="2" fill="#cdb48a"/></svg>
        PHOTOGRAPHY
      </div>
    </div>
    <ul class="contact"><li>dorian@quillfenstudio.com</li><li>www.quillfenstudio.com</li></ul>
    <p class="phone"><svg width="15" height="15" viewBox="0 0 24 24"><path d="M6 2L10 7L8 10Q10 14 14 16L17 14L22 18L19 22Q8 21 2 6Z" fill="#cdb48a"/></svg>778-514-0962</p>
  </section>

  <section class="rack-card rack-card--back">
    <div class="photo photo--entry" role="img" aria-label="Entry hall seen from above with wooden door, staircase and bench"></div>
    <svg class="shapes" viewBox="0 0 322 700" aria-hidden="true">
      <defs>
        <linearGradient id="hdrB" x1="0" y1="0" x2="0" y2="1"><stop offset="0" stop-color="#d8d5d0"/><stop offset="1" stop-color="#fbf9f5"/></linearGradient>
      </defs>
      <path d="M0 0H322V86Q161 130 0 86Z" fill="url(#hdrB)"/>
      <path d="M0 86Q161 130 322 86" stroke="#b08d57" stroke-width="5" fill="none"/>
      <path d="M0 104Q161 132 322 96" stroke="#b08d57" stroke-width="1.5" fill="none"/>
      <path d="M0 382Q161 340 322 382V700H0Z" fill="#fbf9f5"/>
      <path d="M0 378Q161 332 322 378" stroke="#b08d57" stroke-width="5" fill="none"/>
      <path d="M0 365Q161 335 322 370" stroke="#b08d57" stroke-width="1.5" fill="none"/>
      <path d="M0 652Q161 612 322 652V700H0Z" fill="#2a2a2d"/>
      <path d="M0 647Q161 606 322 647" stroke="#b08d57" stroke-width="4" fill="none"/>
    </svg>
    <header class="brand"><span class="brand-mark"></span><span class="brand-name">Quillfen Studio</span></header>
    <h2 class="info-title">Product Information</h2>
    <ul class="info-list">
      <li>Floor Plans measured to QERT &amp; PLUX standards</li>
      <li>Stunning HD Photography</li>
      <li>Vexolith - your space delivered in perfect 3D</li>
      <li>E &amp;O insured</li>
      <li>Our products delivered next by before 10:00 AM</li>
    </ul>
    <div class="partner"><span class="partner-mark"></span><span class="partner-name">vexolith</span></div>
    <ul class="contact"><li>dorian@quillfenstudio.com</li><li>www.quillfenstudio.com</li></ul>
    <p class="phone"><svg width="15" height="15" viewBox="0 0 24 24"><path d="M6 2L10 7L8 10Q10 14 14 16L17 14L22 18L19 22Q8 21 2 6Z" fill="#cdb48a"/></svg>778-514-0962</p>
  </section>

</main>
</body>
</html>
```